Interior designer needs a gorgeous, chic business card design.

A new, small Interior Design firm needs a business card that is chic, contemporary and elegant. Nothing over the top. My interiors are contemporary classic with an elegant feel to them. I like to use quality finishes and products rather than follow the latest fads. Projects can be anything from Pre start selections, bathrooms, kitchens, bedrooms, custom upholstery, furniture, rugs and art etc. The final design should display quality and an achievable sense of chic. I am open to all colours including black but not limited to this.

Business

```html
<!DOCTYPE html>
<html lang="en">
<head>
<meta charset="utf-8">
<title>Velora Interiors — Business Card</title>
<link rel="stylesheet" href="https://fonts.googleapis.com/css2?family=Quicksand:wght@300;400;500&display=swap">
<style>
  :root {
    --page: #ffffff;
    --card: #ffffff;
    --ink: #111111;
    --ink-soft: #2a2a2a;
    --accent: #d2232a;
    --shadow: rgba(0, 0, 0, 0.45);
  }
  * { margin: 0; padding: 0; box-sizing: border-box; }
  html, body {
    width: 1200px;
    height: 900px;
    overflow: hidden;
    background: var(--page);
    font-family: "Quicksand", sans-serif;
    color: var(--ink);
  }
  .canvas {
    position: relative;
    width: 1200px;
    height: 900px;
  }
  .card {
    position: absolute;
    background: var(--card);
    box-shadow: 3px 4px 7px var(--shadow);
  }
  .card--front {
    left: 268px;
    top: 55px;
    width: 637px;
    height: 363px;
  }
  .card--back {
    left: 268px;
    top: 456px;
    width: 639px;
    height: 364px;
  }
  .wordmark {
    position: absolute;
    left: 0;
    right: 0;
    top: 58px;
    text-align: center;
    font-weight: 300;
    color: var(--ink);
    line-height: 1;
  }
  .wordmark__name {
    display: block;
    font-size: 132px;
    letter-spacing: 2px;
  }
  .wordmark__tag {
    display: block;
    margin-top: 22px;
    font-size: 76px;
    letter-spacing: 1px;
  }
  .contact {
    position: absolute;
    left: 59px;
    top: 176px;
  }
  .contact__name {
    font-size: 29px;
    font-weight: 500;
    letter-spacing: 0.3px;
    line-height: 36px;
    color: var(--ink);
  }
  .contact__line {
    font-size: 23px;
    font-weight: 400;
    line-height: 35px;
    color: var(--ink-soft);
    letter-spacing: 0.3px;
  }
  .dot {
    display: inline-block;
    width: 6px;
    height: 6px;
    margin: 0 8px 5px;
    border-radius: 50%;
    background: var(--accent);
    vertical-align: middle;
  }
</style>
</head>
<body>
  <main class="canvas">
    <section class="card card--front" aria-label="Card front">
      <h1 class="wordmark">
        <span class="wordmark__name">Velora</span>
        <span class="wordmark__tag">INTERIORS</span>
      </h1>
    </section>

    <section class="card card--back" aria-label="Card back">
      <div class="contact">
        <p class="contact__name">Marisa Quell Haddon<span class="dot"></span>Director</p>
        <p class="contact__line">Dip. Interior Design</p>
        <p class="contact__line">0400518362<span class="dot"></span>marisa@velorainteriors.com.au</p>
        <p class="contact__line">velorainteriors.com</p>
      </div>
    </section>
  </main>
</body>
</html>
```